Spiritual Healing bussiness needs logo/business card

Simple, clean looking logo/card
For spiritual business with healing services and occult rituals

Contact Information for Business Card

Needs my name: Corwin Halley
Business name: Veyra Healing Shop
Services provided and worded in this way:

Reiki Healing
Tarot
Oils
Rituals Of Change

Can look occult like but with light energy.

Colors
0255a3
3276b5
85abd2
33a6d7
85cae6
0292cd

```html
<!DOCTYPE html>
<html lang="en">
<head>
<meta charset="utf-8">
<title>Veyra Healing Shop — Business Card</title>
<link rel="stylesheet" href="https://fonts.googleapis.com/css2?family=Alegreya+Sans:wght@400;500;700&display=swap">
<style>
  :root {
    --page: #ece9e4;
    --card-top: #acd9d9;
    --card-mid: #7fb0d3;
    --card-bottom: #3476b5;
    --brand-blue: #3a78b6;
    --white: #ffffff;
    --paper: #ffffff;
    --ornament-front: rgba(255, 255, 255, 0.16);
    --ornament-back: rgba(0, 0, 0, 0.05);
    --shadow: 0 6px 14px rgba(0, 0, 0, 0.35);
  }
  * { box-sizing: border-box; margin: 0; padding: 0; }
  html, body { width: 900px; height: 1200px; overflow: hidden; }
  body {
    background: var(--page);
    font-family: "Alegreya Sans", "Trebuchet MS", sans-serif;
    position: relative;
  }
  .card {
    position: absolute;
    left: 85px;
    width: 733px;
    height: 429px;
    border-radius: 22px;
    overflow: hidden;
    box-shadow: var(--shadow);
  }
  .card--front {
    top: 138px;
    background: linear-gradient(180deg, var(--card-top) 0%, var(--card-mid) 45%, var(--card-bottom) 100%);
    color: var(--white);
  }
  .card--back {
    top: 633px;
    background: var(--paper);
  }
  .ornament {
    position: absolute;
  }
  .card--front .ornament {
    right: 0; top: 0;
    width: 290px; height: 429px;
    background: radial-gradient(ellipse at 60% 55%, var(--ornament-front) 0%, rgba(255,255,255,0.05) 60%, transparent 80%);
  }
  .card--back .ornament {
    left: 150px; top: 0;
    width: 470px; height: 429px;
    background: radial-gradient(ellipse at 50% 45%, var(--ornament-back) 0%, rgba(0,0,0,0.02) 60%, transparent 80%);
  }
  .mark {
    position: absolute;
    left: 50%;
    transform: translateX(-50%);
  }
  .card--front .mark { top: 46px; }
  .card--back .mark { top: 112px; }
  .content {
    position: absolute;
    left: 0; right: 0;
    text-align: center;
  }
  .card--front .content { top: 198px; }
  .brand-name {
    font-weight: 400;
    font-size: 42px;
    line-height: 1;
    letter-spacing: 0.2px;
  }
  .services {
    margin-top: 10px;
    font-size: 17px;
    letter-spacing: 0.2px;
  }
  .services .dot { margin: 0 6px; font-size: 12px; vertical-align: 2px; }
  .person {
    margin-top: 18px;
    font-weight: 700;
    font-size: 21px;
    letter-spacing: 0.8px;
  }
  .contact {
    font-size: 18px;
    line-height: 25px;
    margin-top: 2px;
  }
  .card--back .content { top: 270px; }
  .card--back .brand-name {
    font-size: 46px;
    color: var(--brand-blue);
  }
</style>
</head>
<body>
  <section class="card card--front" aria-label="Card front">
    <div class="ornament" role="img" aria-label="Faint flowing ornamental flourish"></div>
    <svg class="mark" width="140" height="140" viewBox="0 0 140 140" aria-hidden="true">
      <circle cx="70" cy="70" r="62" fill="none" stroke="var(--white)" stroke-width="10"/>
    </svg>
    <div class="content">
      <h1 class="brand-name">Veyra Healing Shop</h1>
      <p class="services">Reiki Healing<span class="dot">●</span>Tarot<span class="dot">●</span>Oils<span class="dot">●</span>Rituals Of Change</p>
      <p class="person">CORWIN HALLEY</p>
      <p class="contact">(555) 204-7718</p>
      <p class="contact">Veyrahealingshop@gmail</p>
      <p class="contact">Veyrahealingshop.com</p>
    </div>
  </section>

  <section class="card card--back" aria-label="Card back">
    <div class="ornament" role="img" aria-label="Faint grey ornamental line pattern"></div>
    <svg class="mark" width="136" height="136" viewBox="0 0 136 136" aria-hidden="true">
      <circle cx="68" cy="68" r="60" fill="none" stroke="var(--brand-blue)" stroke-width="10"/>
    </svg>
    <div class="content">
      <h2 class="brand-name">Veyra Healing Shop</h2>
    </div>
  </section>
</body>
</html>
```